Employees at T&M Gale Power Solutions need new modern business cards

We need new business cards that showcase our new rebranded logo. We are seeking modern, clean, fresh, attractive cards while still being professional. We want to stand out. A little bit about us: we work in Canada and the USA. We offer Technical Field Advisors to support wind turbine manufacturers through the construction phase of wind farms. I am attaching a mock inspiration picture to lead you in the direction we want to see this go. Also, FYI We have approx. 10/11 different employees that would need their own card. Let me know when you would need everyone's name. We would love to see some black and white options as well as color copies- when using colors we want green to be the dominant color with accents for blue and orange (colors should match our logo). I have also attached copies of our old business card for reference.

Contact Information for Business Card

Name, Telephone, Email, address, company name, website. EXAMPLE: Hugh Marlow, HughMarlow@tandmgale.example, 555-381-4926, 217763 Birch Line #9, Elmhurst, ON X1Y 2Z3, www.tandmgale.example

Colors
0054AA
0677BA
7BADD7
CADEEF
E8F1F8
00AB8E
00BBA5
67D7C9
C6EFE9
E9F9F6
F0912C
F2A743
F7CA91
FBE8D2
FDF5EE

Requirements
Must have
• 2 sided business card

```html
<!DOCTYPE html>
<html lang="en">
<head>
<meta charset="utf-8">
<title>T&amp;M Gale Power Solutions – Business Card</title>
<link rel="stylesheet" href="https://fonts.googleapis.com/css2?family=Anton&family=Montserrat:wght@400;500;700;800&display=swap">
<style>
  :root{
    --stage:#e6ad6a;
    --card:#fbfbfb;
    --ink:#111111;
    --green:#3aaa35;
    --teal:#00ab8e;
    --teal-dark:#0a9279;
    --teal-light:#67d7c9;
    --yellow:#f7b518;
    --orange:#f2a743;
    --blue:#0677ba;
  }
  *{box-sizing:border-box;margin:0;padding:0}
  html,body{width:1200px;height:706px;overflow:hidden}
  body{background:var(--stage);font-family:"Montserrat",sans-serif;color:var(--ink);position:relative}
  .side-label{position:absolute;top:150px;font-family:"Anton",sans-serif;font-size:28px;letter-spacing:9px;color:#2a2a2a}
  .side-label--front{left:40px}
  .side-label--back{left:620px}
  .card{position:absolute;top:200px;width:540px;height:309px;background:var(--card);overflow:hidden;box-shadow:0 4px 14px rgba(0,0,0,.12)}
  .card--front{left:40px}
  .card--back{left:620px}
  .card__shapes{position:absolute;inset:0;width:100%;height:100%}
  .wordmark{display:flex;align-items:center;gap:10px;font-weight:700;color:var(--green);white-space:nowrap}
  .wordmark__dot{flex:none;border-radius:50%;background:var(--green)}
  .front__brand{position:absolute;left:0;right:0;top:130px;justify-content:center;font-size:26px}
  .front__brand .wordmark__dot{width:16px;height:16px}
  .front__web{position:absolute;left:0;width:540px;top:262px;text-align:center;font-size:16px;font-weight:700}
  .back__brand{position:absolute;left:32px;top:30px;font-size:15px;gap:8px}
  .back__brand .wordmark__dot{width:10px;height:10px}
  .back__name{position:absolute;left:31px;top:118px;font-size:35px;font-weight:800;letter-spacing:.3px;text-transform:uppercase}
  .back__role{position:absolute;left:33px;top:160px;font-size:17px;font-weight:500;color:var(--blue)}
  .contact{position:absolute;left:32px;top:200px;list-style:none;font-size:11px;line-height:1.45}
  .contact__item{display:flex;gap:14px;margin-bottom:10px}
  .contact__icon{width:12px;height:12px;flex:none;margin-top:1px;fill:var(--teal)}
</style>
</head>
<body>
  <div class="side-label side-label--front">FRONT SIDE</div>
  <div class="side-label side-label--back">BACK SIDE</div>

  <section class="card card--front">
    <svg class="card__shapes" viewBox="0 0 540 309" aria-hidden="true">
      <rect x="0" y="0" width="540" height="8" fill="var(--teal)"/>
      <rect x="0" y="301" width="540" height="8" fill="var(--teal)"/>
      <rect x="0" y="8" width="540" height="4" fill="var(--orange)"/>
      <rect x="0" y="297" width="540" height="4" fill="var(--orange)"/>
      <circle cx="40" cy="44" r="6" fill="var(--blue)"/>
      <circle cx="500" cy="265" r="6" fill="var(--orange)"/>
    </svg>
    <div class="wordmark front__brand">
      <span class="wordmark__dot"></span>
      <span>T&amp;M Gale Power Solutions</span>
    </div>
    <div class="front__web">www.tandmgale.example</div>
  </section>

  <section class="card card--back">
    <svg class="card__shapes" viewBox="0 0 540 309" aria-hidden="true">
      <rect x="440" y="0" width="100" height="309" fill="var(--teal)"/>
      <rect x="424" y="0" width="10" height="309" fill="var(--yellow)"/>
      <rect x="440" y="0" width="100" height="110" fill="var(--teal-dark)"/>
    </svg>
    <div class="wordmark back__brand">
      <span class="wordmark__dot"></span>
      <span>T&amp;M Gale Power Solutions</span>
    </div>
    <h1 class="back__name">Hugh Marlow</h1>
    <div class="back__role">Owner</div>
    <ul class="contact">
      <li class="contact__item">
        <svg class="contact__icon" viewBox="0 0 24 24"><path d="M6.6 10.8a15 15 0 0 0 6.6 6.6l2.2-2.2a1 1 0 0 1 1-.25 11.4 11.4 0 0 0 3.6.57 1 1 0 0 1 1 1V20a1 1 0 0 1-1 1A17 17 0 0 1 3 4a1 1 0 0 1 1-1h3.5a1 1 0 0 1 1 1c0 1.25.2 2.45.57 3.57a1 1 0 0 1-.25 1z"/></svg>
        <span>555-381-4926</span>
      </li>
      <li class="contact__item">
        <svg class="contact__icon" viewBox="0 0 24 24"><path d="M2 5h20v14H2z M2 5l10 8 10-8" fill="var(--teal)" stroke="#fff" stroke-width="1.5"/></svg>
        <span>HughMarlow@tandmgale.example</span>
      </li>
      <li class="contact__item">
        <svg class="contact__icon" viewBox="0 0 24 24"><path d="M12 3l10 9h-3v9h-5v-6h-4v6H5v-9H2z"/></svg>
        <span>217763 Birch Line #9<br>Elmhurst, ON X1Y 2Z3, Canada</span>
      </li>
    </ul>
  </section>
</body>
</html>
```